hi all

Im after a new age looking business card with my company logo on it

must include these details, I would like the PH and Email to be symbols

If the colours used for card could be kept within the colours used in logo that I have supplied that would be great, if another colour is to be used dark grey would be ok. no light bulbs etc thanks

Details below to be incorporated on card

Damian Holloway

Lic E871302

PH 0219647381

E info@brightvaleelectrical.example.nz

Domestic Commercial Industrial Electricians

```html
<!DOCTYPE html>
<html lang="en">
<head>
<meta charset="utf-8">
<title>Brightvale Electrical – Business Card</title>
<link href="https://fonts.googleapis.com/css2?family=Montserrat:wght@400;500;600;700&display=swap" rel="stylesheet">
<style>
  :root {
    --bg: #2a2a2a;
    --card-dark: #1e1e1e;
    --card-light: #ffffff;
    --brand-blue: #1a6fbf;
    --ink: #1b1b1b;
    --rule: #9a9a9a;
    --white: #ffffff;
  }
  * { margin: 0; padding: 0; box-sizing: border-box; }
  html, body {
    width: 1200px; height: 895px; overflow: hidden;
    background: var(--bg);
    font-family: "Montserrat", sans-serif;
  }
  .canvas { position: relative; width: 1200px; height: 895px; }
  .card {
    position: absolute; width: 560px; height: 320px;
    overflow: hidden;
    box-shadow: 0 10px 30px rgba(0,0,0,.45);
  }
  .card svg.card-shapes { position: absolute; inset: 0; }
  .card-front { left: 30px; top: 287px; background: var(--card-dark); }
  .card-back  { left: 610px; top: 287px; background: var(--card-light); }

  .brand {
    position: absolute; left: 0; right: 0;
    display: flex; align-items: center; justify-content: center; gap: 14px;
    color: var(--brand-blue); font-weight: 700; letter-spacing: 2px;
    text-transform: uppercase;
  }
  .brand-name { width: min-content; line-height: 1.1; text-align: left; }
  .brand-dot { flex: none; display: inline-block; border-radius: 50%; background: var(--brand-blue); }
  .card-front .brand { top: 48px; font-size: 34px; }
  .card-front .brand-dot { width: 44px; height: 44px; }
  .card-back .brand { top: 30px; font-size: 26px; }
  .card-back .brand-dot { width: 34px; height: 34px; }

  .holder-name {
    position: absolute; left: 0; right: 0; top: 124px; text-align: center;
    color: var(--brand-blue); font-weight: 600; font-size: 22px; letter-spacing: 1px;
    text-transform: uppercase;
  }
  .holder-rule {
    position: absolute; left: 205px; width: 150px; top: 160px;
    border-top: 1px solid var(--rule);
  }
  .contact {
    position: absolute; top: 182px; left: 0; right: 0;
    display: flex; justify-content: center; gap: 22px;
    color: var(--ink); font-size: 13px; font-weight: 500;
  }
  .contact-item { display: flex; align-items: center; gap: 7px; white-space: nowrap; }
  .contact-item svg { width: 14px; height: 14px; fill: var(--brand-blue); }
  .licence {
    position: absolute; right: 70px; bottom: 22px;
    color: var(--white); font-size: 14px; letter-spacing: 2px;
  }
</style>
</head>
<body>
<main class="canvas">

  <section class="card card-front" aria-label="Card front">
    <svg class="card-shapes" viewBox="0 0 560 320" width="560" height="320">
      <path class="swoosh-white" d="M0,292 Q280,170 560,122 Q280,180 0,300 Z" fill="var(--white)"/>
      <path class="service-band" d="M0,306 Q280,190 560,140 L560,172 Q300,218 0,320 Z" fill="var(--brand-blue)"/>
      <path id="band-text-path" d="M60,300 Q300,196 560,156" fill="none"/>
      <text class="services" font-family="Montserrat, sans-serif" font-weight="600" font-size="13" fill="var(--white)" letter-spacing="0.5">
        <textPath href="#band-text-path" startOffset="8%">Domestic Commercial Industrial Electricians</textPath>
      </text>
    </svg>
    <div class="brand"><span class="brand-dot"></span><span class="brand-name">Brightvale Electrical</span></div>
  </section>

  <section class="card card-back" aria-label="Card back">
    <svg class="card-shapes" viewBox="0 0 560 320" width="560" height="320">
      <path class="footer-dark" d="M0,320 Q300,302 560,208 L560,320 Z" fill="var(--card-dark)"/>
      <path class="swoosh-blue" d="M0,318 Q300,292 560,196 L560,204 Q300,300 0,320 Z" fill="var(--brand-blue)"/>
    </svg>
    <div class="brand"><span class="brand-dot"></span><span class="brand-name">Brightvale Electrical</span></div>
    <div class="holder-name">Damian Holloway</div>
    <div class="holder-rule"></div>
    <div class="contact">
      <span class="contact-item">
        <svg viewBox="0 0 24 24" aria-label="Phone"><path d="M6.6 10.8a15.1 15.1 0 0 0 6.6 6.6l2.2-2.2c.3-.3.7-.4 1-.2 1.1.4 2.3.6 3.6.6.6 0 1 .4 1 1V20c0 .6-.4 1-1 1A17 17 0 0 1 3 4c0-.6.4-1 1-1h3.5c.6 0 1 .4 1 1 0 1.3.2 2.5.6 3.6.1.3 0 .7-.2 1z"/></svg>
        0219647381
      </span>
      <span class="contact-item">
        <svg viewBox="0 0 24 24" aria-label="Email"><path d="M2 5h20v14H2z M2 5l10 8 10-8" fill="none" stroke="var(--brand-blue)" stroke-width="2"/></svg>
        info@brightvaleelectrical.example.nz
      </span>
    </div>
    <div class="licence">Lic E871302</div>
  </section>

</main>
</body>
</html>
```